Vice chair

I'm running for a position as vice chair this will be posted in the lunch room cafeteria in this package i posted logos, my picture, sample of old flyers to give you a idea i also wrote literature need help in putting it together like it to look like a million bucks goal win this election I summited lots of pdf files and jpeg look though them to help with your design feel free to contact me to further assist you
Updates

Would like this to be completed by Wednesday

Target Market(s)

My constituents

Font styles to use
Serif

Colors

Designer to choose colors to be used in the design.

Requirements
Must have
• Make it look clean neat
Nice to have
• Nice background

```html
<!DOCTYPE html>
<html lang="en">
<head>
<meta charset="utf-8">
<title>Vote for Marco Delgado as Vice Chair</title>
<link href="https://fonts.googleapis.com/css2?family=Bebas+Neue&family=Roboto+Slab:wght@300;400;700&display=swap" rel="stylesheet">
<style>
  :root {
    --navy: #000a8c;
    --red: #ff0a0a;
    --white: #ffffff;
    --panel-grey: #e4e4e4;
    --page: #ffffff;
    --edge: #e6e6e6;
  }
  * { margin: 0; padding: 0; box-sizing: border-box; }
  html, body { width: 1200px; height: 826px; overflow: hidden; background: var(--page); }
  .flyer {
    position: relative; width: 1200px; height: 826px;
    background: var(--page); border: 1px solid var(--edge);
    font-family: "Roboto Slab", Georgia, serif;
  }
  .star-row {
    position: absolute; left: 93px; width: 1022px;
    display: flex; justify-content: space-between;
    font-size: 29px; line-height: 1;
  }
  .star-row.top { top: 34px; }
  .star-row.bottom { top: 760px; }
  .star-group { display: flex; gap: 8px; }
  .star-group.red { color: var(--red); }
  .star-group.blue { color: var(--navy); }

  .slogan-panel {
    position: absolute; left: 95px; top: 76px; width: 389px; height: 664px;
    background: var(--navy);
  }
  .slogan {
    position: absolute; left: 40px; top: 36px;
    font-family: "Bebas Neue", Impact, sans-serif;
    font-size: 90px; line-height: 75.5px; color: var(--white);
  }
  .slogan .accent { color: var(--red); }
  .slogan span { display: block; }

  .info-panel {
    position: absolute; left: 484px; top: 76px; width: 620px; height: 664px;
    background: var(--panel-grey);
  }
  .panel-stars {
    position: absolute; left: 549px; top: 112px;
    color: var(--red); font-size: 33px; letter-spacing: 8px; line-height: 1;
  }
  .badges { position: absolute; left: 820px; top: 106px; }
  .name-band {
    position: absolute; left: 484px; top: 163px; width: 620px; height: 112px;
    background: var(--navy);
  }
  .candidate-name {
    position: absolute; left: 518px; top: 184px;
    font-family: "Roboto Slab", Georgia, serif; font-weight: 700;
    font-size: 57px; line-height: 1; color: var(--white); letter-spacing: 1px;
  }
  .vote-badge {
    position: absolute; left: 379px; top: 155px; width: 129px; height: 129px;
    border-radius: 50%; background: var(--white);
    display: flex; align-items: center; justify-content: center;
    font-family: "Bebas Neue", Impact, sans-serif; font-size: 38px;
    color: var(--red); letter-spacing: 0;
  }
  .role-box {
    position: absolute; left: 484px; top: 276px; width: 346px; height: 72px;
    background: var(--red); color: var(--white);
    font-weight: 700; font-size: 36px; line-height: 72px; padding-left: 39px;
  }
  .portrait {
    position: absolute; left: 797px; top: 294px; width: 307px; height: 446px;
    background: linear-gradient(160deg, #3a2a22 0%, #8a5a40 45%, #1a1a1a 80%);
    border-radius: 48% 44% 0 0 / 30% 30% 0 0;
  }
  .message { position: absolute; left: 508px; color: var(--red); }
  .message.intro {
    top: 383px; width: 255px; font-weight: 300; font-size: 11.2px; line-height: 13.5px;
  }
  .message.pitch {
    top: 493px; width: 265px; font-weight: 700; font-size: 11px; line-height: 13.4px;
  }
  .message.appeal {
    top: 585px; width: 265px; font-weight: 400; font-size: 17.6px; line-height: 21.5px;
  }
</style>
</head>
<body>
<div class="flyer">
  <div class="star-row top" aria-hidden="true">
    <div class="star-group red"><span>★</span><span>★</span><span>★</span><span>★</span><span>★</span></div>
    <div class="star-group blue"><span>★</span><span>★</span><span>★</span><span>★</span><span>★</span></div>
    <div class="star-group blue"><span>★</span><span>★</span><span>★</span><span>★</span><span>★</span></div>
    <div class="star-group red"><span>★</span><span>★</span><span>★</span><span>★</span><span>★</span></div>
    <div class="star-group red"><span>★</span><span>★</span><span>★</span><span>★</span><span>★</span></div>
    <div class="star-group blue"><span>★</span><span>★</span><span>★</span><span>★</span><span>★</span></div>
  </div>

  <section class="slogan-panel">
    <h2 class="slogan">
      <span>Bring</span><span>Change</span>
      <span class="accent">Bring</span><span class="accent">Trust</span>
      <span>Bring</span><span>Progress</span>
      <span class="accent">Bring</span><span class="accent">New Vision</span>
    </h2>
  </section>

  <section class="info-panel"></section>
  <div class="panel-stars" aria-hidden="true">★★★★★</div>
  <svg class="badges" width="250" height="72" viewBox="0 0 250 72" role="img" aria-label="Depot badges">
    <circle cx="36" cy="36" r="35" fill="#1a50c8"/>
    <circle cx="123" cy="36" r="35" fill="#f2e400" stroke="#222" stroke-width="2"/>
    <circle cx="207" cy="36" r="35" fill="#f07a1a" stroke="#222" stroke-width="2"/>
  </svg>

  <div class="name-band"></div>
  <h1 class="candidate-name">MARCO DELGADO</h1>
  <div class="vote-badge">VOTE FOR</div>
  <div class="role-box">As VICE CHAIR</div>

  <div class="portrait" role="img" aria-label="Portrait photo of the candidate"></div>

  <p class="message intro">I Marco Delgado for those who dont know me would like to introduce myself. I have always been approachable and helpful whether you are a probationary officer or a veteran operator with knowledge or information. We must protect our union rules for ourselves, our future and most important our children</p>
  <p class="message pitch">I would like this opportunity to run as your vice chair a person you can trust and believe in me Positive and motivations are my main keys for progress and for change in my campaign. when there are no leaders to look up to one therefore must become one.</p>
  <p class="message appeal">I do believe I ‘m the right person for this position so please come out and support me and vote me as your vice chair</p>

  <div class="star-row bottom" aria-hidden="true">
    <div class="star-group red"><span>★</span><span>★</span><span>★</span><span>★</span><span>★</span></div>
    <div class="star-group blue"><span>★</span><span>★</span><span>★</span><span>★</span><span>★</span></div>
    <div class="star-group blue"><span>★</span><span>★</span><span>★</span><span>★</span><span>★</span></div>
    <div class="star-group red"><span>★</span><span>★</span><span>★</span><span>★</span><span>★</span></div>
    <div class="star-group red"><span>★</span><span>★</span><span>★</span><span>★</span><span>★</span></div>
    <div class="star-group blue"><span>★</span><span>★</span><span>★</span><span>★</span><span>★</span></div>
  </div>
</div>
</body>
</html>
```